We need a web design for our business in which we provide complete network packages.

Hello Designers!

First, we’d like to make clear that rather than simple web design contents. We want someone that can help design our visual branding, help us communicate a sentiment. And we are willing to pay for that.

Who are we?

We are Velcor Hub. Our company is based in Rotterdam, the Netherlands. We are providing a unique full-service concept for (wireless) communication networks within small to mid-range businesses. This means we will not only provide the hardware needed for a fast and secure network within a company, but will also install, optimize, support and maintain it. 

Velcor Hub is a new brand of a company called Trindle Works which has over 15 years of experience in the market of customer service and support. Velcor Hub is the first satellite of more to come. Like Kobi Depot and others Planets, all have a focus on full service solutions.

Velcor Hub has an experienced support center from which we can monitor our clients network in real time. Our clients don’t have to worry about anything, if something is not working correctly, we will fix it pro actively. Our clients range from education and training facilities, catering, industry, logistics, health care, consultancy agencies and high end consumers. 

In an overview all Unique Selling Points of Velcor Hub:
• Professional service, both on location and remote!
• Direct clear price indication via our unique business configuration wizard
• A specific and complete quotation after a personal intake, within two days.
• Backed by a professional call center open 12 hours a day and open on Saturdays as well.
• Backed by a professional repair center with more than 15 years of experience.
• Installation and configuration included.
• Optimization included within the first three months powered by AI and machine learning.
• Real time remote maintenance. Quality control, security and interference.

Logo
For our business we need a logo. The logo needs to tell what we stand for and what we do. It will be used in both online and offline communication to our customers. Mainly e-mail and digital forms. As Velcor Hub is one of the branches within our company we would like the logo to be part of a series in the future, which should be recognizable as part of a group of websites/brands.

Website
For our business we need a website.  The website needs a story and matching design and this is where you come in. The main focus of this website is to provide information, but more importantly to guide the user to our special quotation business configuration wizard. This business configuration wizard allows users to fill in information about their business and wish requirements, at which they will receive a real time price indication on completion. 

Configuration wizard
This business configuration wizard is developed separately by our own development team but should be part of the website in look and feel.. Our development team will develop the business configuration wizard and embed it in the website. 
The setup of the website should be focused on leading all visitors to the business configuration wizard which we create our quality leads. The website will inform the possible customers/leads on the unique selling points and then remind the customer to use the business configuration wizard to get a direct price indication. 

For the website and logo we need the whole package, the design you are creating needs to have returning elements like fonts, icons, color use,  images, maybe even characters etc. You name it! 
There needs to be a common thread in the design so we can reuse elements in, for example, the email templates, the work order or receipt we give to our customers (we may contact the winner of the contest to design these for us as well!). 

The layout needs to be complete. We want something modern. A one page design that is bright and colorful with collapsing area’s to show more information. 

Website wishes and requirements
The process:
The main function of our website, besides giving a clear indication what we do, will be to guide the user to our ‘business configuration wizard’. 

Website functionality:
Our website will be our main form of communication. We need a main/front page designed in a long single scrolling page style. Users can click on buttons to view more information. Information that was hidden before. We have included our own temporary mock ups to give you an idea of the flow we desire for the website. The titles and headers in these mock ups are in Dutch but we will translate this in the description below. These mock ups are just that, an idea about the visual presentation. You are free to implement your own design, fonts, icons, pictures etc.

The page will have 6 different areas (beside the top ‘hero’ part) and a final 7th area which is the “end page” and is a big business configuration wizard promotion.In each area you are pointed towards the business configuration wizard but if you scroll all the way down you will end up with this 7th area which is all about the wizard. However these 6 areas will need to be ‘expandable/collapsible’, meaning the user can click a “read more” button at which the element will expand to show extra information beneath it. The user can then collapse this element again by closing the part that just opened.

1. Top/Hero - Customers will be able to configure their own price indication through our wizard. So there will need to be a prominent button at the top of our main page and on the 7th area that will bring the customer to this wizard/application. This will need to be a focus throughout the whole website, meaning this button is a returning element. Furthermore the top needs two menus. One for navigating the main page itself, the other one is for switching between the different industry ‘flavors’ (Education, Logistics, Health Care etc). The idea is that the photos and text on the website will change depending on the industry picked. The design and layout remains the same however. The mock ups are based on ‘education’ and another based on logistics.

2. Real time Maintenance (Beheer) – This will be a collapsible component. It will provide a brief description of our maintenance service. The ‘configure now!’ button will need to be displayed in this area as well. This component is collapsible, meaning the user can click on a ‘Read more’ (Dutch: lees meer) button at which the element will open up to show extra information (2.1).
2.1 The extra information that can be collapsed by clicking the ‘X’ button. The headers on this page read “Carefree real time maintenance”, “Certified team of administrators”, “High service level”, “Defects immediately detected”, “Continuous remote maintenance”.

3.  Service range (Bereik) - This will be a collapsible component. It will provide a brief description of how we provide for enough wifi range within a building or company. The ‘configure now!’ button will need to be displayed in this area as well. This component is collapsible, meaning the user can click on a ‘Read more’ (Dutch: lees meer) button at which the element will open up to show extra information (3.1).
3.1 The extra information that can be collapsed by clicking the ‘X’ button. The headers on this page read “Enough range everywhere”, “Machine learning for maximum range”, “Different types of access points”, “Beamforming & Mu-MiMo”, “Multiple locations connected”.

4. Speed (Snelheid) -  This is the only component that needs to collapse twice. It will provide a brief description of how we will guarantee the fastest network speed possible. The ‘configure now!’ button will need to be displayed in this area as well. This component is collapsible, meaning the user can click on a ‘Read more’ (Dutch: lees meer) button at which the element will open up to show extra information (4.1).
4.1 The extra information that can be collapsed by clicking the ‘X’ button. The headers on this page read “Band steering, “Airtime fairness”, “Load balancing”. The user will be able to open up another element to show even more information (4.2).
4.2 This will mainly show the diagrams shown in the mock ups. It will provide extra information on what is meant by “Airtime fairness” and “Load balancing”.

5.  Manageable Costs (Beheersbare kosten) - This will be a collapsible component. It will provide a brief description of how users can manage their own costs. The ‘configure now!’ button will need to be displayed in this area as well. This component is collapsible, meaning the user can click on a ‘Read more’ (Dutch: lees meer) button at which the element will open up to show extra information (5.1).
5.1 The extra information that can be collapsed by clicking the ‘X’ button. The headers on this page read “Manageable costs”, “Upfront insight in predicated costs”, “Best price/quality ratio”, “10 years of warranty”, “High availability”.

6.  Protected and secure (Beschermd en veilig) -  This will be a collapsible component. It will provide a brief description of our protection and security guaranties. The ‘configure now!’ button will need to be displayed in this area as well. This component is collapsible, meaning the user can click on a ‘Read more’ (Dutch: lees meer) button at which the element will open up to show extra information (6.1).
6.1 The extra information that can be collapsed by clicking the ‘X’ button. The headers on this page read “Protected and Secure”, “Protected by Zenthro”, “Fire resistant and dust free”, “Managed and maintained in the Netherlands”.

7. Extras (Extra’s) - This will be a collapsible component. It will provide a brief description of additional options which our solution can provide. The ‘configure now!’ button will need to be displayed in this area as well. This component is collapsible, meaning the user can click on a ‘Read more’ (Dutch: lees meer) button at which the element will open up to show extra information (7.1).
7.1 The extra information that can be collapsed by clicking the ‘X’ button. The headers on this page read “Connection with portals like Lumigram”, “Everything in one cable”, “Cloud ready”, “Ready for even more?”.

8. unique business configuration wizard - This is the final page to (once again!) push the visitor to the ‘configure now!’ button showing some reasons to click right now.

For now, we need a logo and a website designed. We would also like a design for the configuration wizard in the same style as the website.

What we'd like:
- A modern professional, but fun, appearance
- Elements like icons to have a flat design.
- Website can be used for the different industry flavors (for example, our mockups are geared towards clients in the education sector, but we can simply swap some of the photos and content to reflect the health care sector).
- Keep in mind that the website will need to be responsive when designing!
- Create a fun and trustworthy feeling.

We will be able to provide stock photographs if necessary!

Velcor Hub

```html
<!DOCTYPE html>
<html lang="en">
<head>
<meta charset="utf-8">
<title>Velcor Hub – Professional Services</title>
<link href="https://fonts.googleapis.com/css2?family=Poppins:wght@300;400;500;600;700&display=swap" rel="stylesheet">
<style>
:root{
  --stage:#e6e6e6;
  --white:#ffffff;
  --ink:#2b2940;
  --muted:#9a9cb2;
  --soft:#f2f6fa;
  --hero-top:#6f6c93;
  --hero-bottom:#2c2a40;
  --blue:#4ab3d6;
  --orange:#f25a2a;
  --violet:#7b6cf6;
  --link:#5b6bd8;
  --cyan:#3fd0d9;
  --cyan-soft:#e4f9fa;
  --yellow:#f7ea3a;
  --cta:#35334f;
  --footer:#34315a;
  --footer-text:#a8a6d6;
}
*{box-sizing:border-box;margin:0;padding:0}
html,body{width:1200px;height:2947px;overflow:hidden}
body{background:var(--stage);font-family:'Poppins',sans-serif;color:var(--ink);position:relative}
.page{position:absolute;left:138px;top:138px;width:922px;background:var(--white)}
section,header,footer{position:relative;width:922px}
.abs{position:absolute}

/* hero */
.hero{height:270px;background:linear-gradient(180deg,var(--hero-top),var(--hero-bottom));overflow:hidden;color:var(--white)}
.hero-art{position:absolute;left:0;bottom:0;width:922px;height:150px;background:linear-gradient(90deg,#e3484f 0%,#8f3048 30%,#3a2f4b 55%,#7a2e42 80%,#3a3350 100%);opacity:.9}
.hero-curve{position:absolute;left:0;bottom:0}
.brand{display:flex;align-items:center;gap:6px;font-weight:600;font-size:14px;color:var(--white)}
.brand-mark{width:14px;height:14px;border-radius:50%;background:var(--violet)}
.nav{position:absolute;top:26px;right:190px;display:flex;gap:20px;font-size:8.5px;font-weight:600}
.nav .new{position:relative}
.nav .new::before{content:"New";position:absolute;top:-10px;left:30px;background:var(--yellow);color:var(--ink);font-size:6px;padding:0 4px;border-radius:6px}
.signin{position:absolute;right:86px;top:16px;width:67px;height:16px;border-radius:8px;background:var(--yellow);color:var(--ink);font-size:8px;text-align:center;line-height:16px}
.phone{position:absolute;right:96px;top:37px;font-size:8px;font-weight:600}
.hero-kicker{position:absolute;top:106px;width:100%;text-align:center;font-size:8.5px;opacity:.85}
.hero-title{position:absolute;top:124px;width:100%;text-align:center;font-size:24px;font-weight:700;letter-spacing:.3px}
.crumb{position:absolute;top:167px;width:100%;text-align:center;font-size:9.5px}
.crumb span{color:#4b6cff}

/* promises + pricing */
.offer{height:449px}
.promise{position:absolute;top:36px;display:flex;gap:12px;align-items:center}
.hex{width:34px;height:34px;background:var(--cyan-soft);clip-path:polygon(50% 0,93% 25%,93% 75%,50% 100%,7% 75%,7% 25%);display:flex;align-items:center;justify-content:center;color:var(--cyan);font-weight:700;font-size:14px}
.promise h4{font-size:8.5px;font-weight:600}
.promise p{font-size:7.5px;color:var(--muted);font-weight:300}
.plan{position:absolute;top:110px;width:236px;height:304px;background:#f7f9fb;text-align:center}
.plan-head{height:71px;color:var(--white);padding-top:8px}
.plan-head small{font-size:7.5px;display:block}
.plan-head strong{font-size:20px;font-weight:600;display:block;margin-top:6px}
.plan ul{list-style:none;padding-top:14px;font-size:8.5px;color:#4a4a5e;line-height:21px}
.plan-btn{display:inline-block;margin-top:12px;width:85px;height:23px;border-radius:4px;color:var(--white);font-size:8px;font-weight:600;line-height:23px;letter-spacing:.4px}
.plan.regular .plan-head,.plan.regular .plan-btn{background:var(--blue)}
.plan.better .plan-head,.plan.better .plan-btn{background:var(--orange)}

/* features */
.features{height:481px;background:var(--white)}
.features-bg{position:absolute;left:0;top:0}
.features h2{position:absolute;top:150px;width:100%;text-align:center;font-size:19px;font-weight:500}
.feature{position:absolute;width:225px}
.feature svg{position:absolute;left:0;top:0}
.feature h4{margin-left:47px;font-size:9.5px;font-weight:500}
.feature p{margin-left:47px;margin-top:5px;font-size:8.5px;color:var(--muted);line-height:14px;font-weight:300}

/* story */
.story{height:501px;border-bottom:1px solid #f1f1f4}
.story-art{position:absolute;left:121px;top:100px;width:397px;height:322px;border-radius:50% 50% 8px 8px/40% 40% 8px 8px;background:linear-gradient(135deg,#f2f4f8 0%,#e7ebf2 60%,#f6e2d6 100%)}
.story h3{position:absolute;left:599px;top:122px;font-size:17px;font-weight:600;line-height:22px}
.story .lead{position:absolute;left:599px;top:180px;width:250px;font-size:9.5px;color:var(--muted);line-height:19.5px;font-weight:300}
.story .lead b{color:var(--ink);font-weight:600}
.story .body{position:absolute;left:599px;top:230px;width:245px;font-size:9.5px;color:var(--muted);line-height:19.5px;font-weight:300}
.story-btn{position:absolute;left:599px;top:340px;width:110px;height:28px;background:var(--white);box-shadow:0 6px 18px rgba(40,40,80,.08);font-size:9px;color:var(--link);text-align:center;line-height:28px}

/* faq */
.faq{height:320px}
.faq h2{position:absolute;top:64px;width:100%;text-align:center;font-size:16.5px;font-weight:500}
.faq-item{position:absolute;left:163px;font-size:9.5px;font-weight:500}
.faq-item .sign{display:inline-block;width:20px}
.faq-item.open{color:var(--violet)}
.faq-answer{position:absolute;left:183px;top:140px;width:570px;font-size:9px;color:var(--muted);line-height:17px;font-weight:300}

/* cta */
.cta{height:181px;background:var(--cta);color:var(--white)}
.cta h3{position:absolute;left:86px;top:46px;font-size:13px;font-weight:600}
.cta p{position:absolute;left:86px;top:68px;width:500px;font-size:9px;line-height:18px;color:#b9b7e0;font-weight:300}
.pill{position:absolute;top:70px;height:27px;border-radius:14px;font-size:8px;text-align:center;line-height:27px}
.pill.signup{left:640px;width:75px;background:var(--violet);color:var(--white)}
.pill.login{left:724px;width:70px;background:var(--white);color:var(--violet)}

/* footer */
.site-footer{height:460px;background:var(--footer);color:var(--white)}
.site-footer h4{position:absolute;font-size:11px;font-weight:600}
.links{position:absolute;top:102px;list-style:none;font-size:8.5px;color:var(--footer-text);line-height:23px}
.links li::before{content:"•";color:var(--violet);margin-right:10px}
.badge{position:absolute;background:#4b4878;border-radius:4px}
.demo-note{position:absolute;left:670px;top:170px;font-size:7px;color:var(--footer-text)}
.contact-box{position:absolute;left:670px;width:173px;height:44px;background:var(--white);border-radius:3px;color:var(--ink);padding:10px 14px;font-size:7.5px;letter-spacing:.5px}
.contact-box strong{display:block;color:var(--cta);font-weight:600;margin-top:2px}
.foot-brand{position:absolute;left:77px;top:349px;display:flex;gap:6px;align-items:center;font-weight:600;font-size:15px;color:#9d9ce0}
.foot-brand i{width:18px;height:18px;background:#9d9ce0;border-radius:4px}
.socials{position:absolute;left:77px;top:384px;display:flex;gap:12px}
.socials i{width:13px;height:13px;border-radius:50%;background:#4b4878}
.foot-nav{position:absolute;font-size:7.5px;color:var(--footer-text);letter-spacing:.3px}
.copyright{position:absolute;left:77px;top:430px;font-size:7.5px;color:#7e7cb0}
.locale{position:absolute;left:717px;top:429px;font-size:7.5px;color:var(--footer-text);display:flex;gap:12px}
.to-top{position:absolute;left:868px;top:419px;width:24px;height:24px;border-radius:50%;background:#2a2848}
</style>
</head>
<body>
<div class="page">

  <header class="hero">
    <div class="hero-art" role="img" aria-label="Illustrated red and plum mountain range under a dusk sky"></div>
    <svg class="hero-curve" width="922" height="60" viewBox="0 0 922 60"><path d="M0 60 L0 35 C260 60 620 55 922 0 L922 60 Z" fill="#fff"/></svg>
    <div class="brand abs" style="left:86px;top:24px"><span class="brand-mark"></span>Velcor Hub</div>
    <nav class="nav"><span>Home</span><span>Services</span><span class="new">Excellence</span><span>Help</span><span>Contact us</span></nav>
    <div class="signin">sign in</div>
    <div class="phone">24810-3377</div>
    <div class="hero-kicker">Best Network Installation 2020 Brightlist</div>
    <h1 class="hero-title">PROFESSIONAL SERVICES</h1>
    <div class="crumb"><span>homepage</span> - professional services</div>
  </header>

  <section class="offer">
    <div class="promise" style="left:96px"><div class="hex">$</div><div><h4>30DAYS MONEY BACK</h4><p>is simply dummy text of the printing</p></div></div>
    <div class="promise" style="left:353px"><div class="hex"><svg width="14" height="14" viewBox="0 0 14 14"><path d="M2 7 L6 11 L12 3" fill="none" stroke="currentColor" stroke-width="2"/></svg></div><div><h4>SECURE PAYMENT TRANSACTION</h4><p>is simply dummy text of the printing</p></div></div>
    <div class="promise" style="left:609px"><div class="hex"><svg width="14" height="14" viewBox="0 0 14 14"><circle cx="7" cy="7" r="5" fill="none" stroke="currentColor" stroke-width="2.5"/></svg></div><div><h4>FAST SUPPORT RESPONDING</h4><p>is simply dummy text of the printing</p></div></div>

    <div class="plan regular" style="left:214px">
      <div class="plan-head"><small>Regular Installation</small><strong>$100</strong></div>
      <ul><li>lorem ipsum dollor sit</li><li>ammet constectur addispicing</li><li>elit errun nisi uels</li><li>dollorum repealis</li><li>officia neque script</li><li>nihil incidunt</li><li>corporis asperioes telemanta</li><li>culpa essae excepturi molestasi</li></ul>
      <span class="plan-btn">ADD TO CART</span>
    </div>
    <div class="plan better" style="left:471px">
      <div class="plan-head"><small>Better Installation</small><strong>$150</strong></div>
      <ul><li>lorem ipsum dollor sit</li><li>ammet constectur addispicing</li><li>elit errun nisi uels</li><li>dollorum repealis</li><li>officia neque script</li><li>nihil incidunt</li><li>corporis asperioes telemanta</li><li>culpa essae excepturi molestasi</li></ul>
      <span class="plan-btn">ADD TO CART</span>
    </div>
  </section>

  <section class="features">
    <svg class="features-bg" width="922" height="481" viewBox="0 0 922 481"><path d="M0 62 C120 90 260 0 330 40 C400 80 450 130 560 110 C700 80 780 10 922 0 L922 481 L0 481 Z" fill="#f2f6fa"/></svg>
    <h2>Simple and Powerful</h2>
    <div class="feature" style="left:86px;top:232px"><svg width="28" height="28" viewBox="0 0 28 28" fill="none" stroke="#3a6fd8" stroke-width="1.6"><rect x="2" y="2" width="24" height="24" rx="3"/><circle cx="14" cy="14" r="7"/><circle cx="11" cy="14" r="1" fill="#3a6fd8"/><circle cx="17" cy="14" r="1" fill="#3a6fd8"/></svg><h4>Stay connected all the time</h4><p>Lorem ipsum dolor sit amet consectetur adipisicing elit. Dolores rem reiciendis illum nulla nam ipsum quae eaque</p></div>
    <div class="feature" style="left:343px;top:232px"><svg width="28" height="28" viewBox="0 0 28 28" fill="none" stroke="#3a6fd8" stroke-width="1.6"><rect x="2" y="15" width="24" height="7" rx="1"/><path d="M6 15 L3 5 M22 15 L25 5"/></svg><h4>No noisy neighbors</h4><p>Lorem ipsum dolor sit amet consectetur adipisicing elit. Dolores rem reiciendis illum nulla nam ipsum quae eaque</p></div>
    <div class="feature" style="left:599px;top:232px"><svg width="28" height="28" viewBox="0 0 28 28" fill="none" stroke="#3a6fd8" stroke-width="1.6"><rect x="3" y="14" width="22" height="8" rx="3"/><path d="M9 9 C12 6 16 6 19 9 M11 11 C13 10 15 10 17 11"/></svg><h4>Powerful infrastructure</h4><p>Lorem ipsum dolor sit amet consectetur adipisicing elit. Dolores rem reiciendis illum nulla nam ipsum quae eaque</p></div>
    <div class="feature" style="left:86px;top:336px"><svg width="28" height="28" viewBox="0 0 28 28" fill="none" stroke="#3a6fd8" stroke-width="1.6"><path d="M9 3 V9 M19 3 V9 M7 9 H21 V17 C21 21 18 23 14 23 C10 23 7 21 7 17 Z M14 23 V27"/></svg><h4>Many OS combinations</h4><p>Lorem ipsum dolor sit amet consectetur adipisicing elit. Dolores rem reiciendis illum nulla nam ipsum quae eaque</p></div>
    <div class="feature" style="left:343px;top:336px"><svg width="28" height="28" viewBox="0 0 28 28" fill="none" stroke="#3a6fd8" stroke-width="1.6"><path d="M4 24 L24 4 M10 10 L18 18 M8 14 L14 8 M14 20 L20 14"/></svg><h4>Root administrator access</h4><p>Lorem ipsum dolor sit amet consectetur adipisicing elit. Dolores rem reiciendis illum nulla nam ipsum quae eaque</p></div>
    <div class="feature" style="left:599px;top:336px"><svg width="28" height="28" viewBox="0 0 28 28" fill="none" stroke="#3a6fd8" stroke-width="1.6"><path d="M4 24 L10 18 M10 18 L18 10 L22 14 L14 22 Z M18 10 L24 4"/></svg><h4>No long term contracts</h4><p>Lorem ipsum dolor sit amet consectetur adipisicing elit. Dolores rem reiciendis illum nulla nam ipsum quae eaque</p></div>
  </section>

  <section class="story">
    <div class="story-art" role="img" aria-label="Illustration of three colleagues working together at a computer desk beside a plant"></div>
    <h3>We are with you ,<br>every step of the way</h3>
    <p class="lead">Whether you are looking for a <b>personal</b> website hosting plan or a <b>business</b> website hosting plan.</p>
    <p class="body">Lorem ipsum dolor sit amet consectetur adipisicing elit. Eum, nisi eius dolorum repellat officia neque suscipit facere quia quod, nihil incidunt corporis asperiores dolorem obcaecati molestiae, culpa esse excepturi molestias!</p>
    <div class="story-btn">start with us now</div>
  </section>

  <section class="faq">
    <h2>Frequently Asked Questions.</h2>
    <div class="faq-item open" style="top:115px"><span class="sign">—</span>How Can I Order ?</div>
    <p class="faq-answer">Lorem ipsum dolor sit amet consectetur adipisicing elit. Iure perspiciatis similique repellendus, in excepturi mollitia consectetur consequatur soluta labore, a pariatur et dolore saepe fugit fuga qui harum atque. Sunt.</p>
    <div class="faq-item" style="top:202px"><span class="sign">+</span>What Is Velcor Hub ?</div>
    <div class="faq-item" style="top:229px"><span class="sign">+</span>I Want New order</div>
  </section>

  <section class="cta">
    <h3>Order Now And Get The Most Service</h3>
    <p>Lorem ipsum dolor sit amet consectetur, adipisicing elit. Rerum recusandae iusto, soluta eos ullam corporis! In veniam repudiandae maiores numquam consectetur vitae suscipit sint inventore, excepturi magni a, aliquid est.</p>
    <span class="pill signup">SIGN UP</span>
    <span class="pill login">LOG IN</span>
  </section>

  <footer class="site-footer">
    <h4 style="left:86px;top:68px">Quick Links</h4>
    <ul class="links" style="left:74px"><li>Services Installation</li><li>Optimize</li><li>Maintenance</li><li>Support</li><li>Professional Services</li><li>Clear Price Indication</li><li>Spesific And Complete</li><li>12 Hours Support</li><li>Experienced</li></ul>
    <ul class="links" style="left:362px"><li>Contact Us</li><li>Help</li><li>Forgot Password?</li><li>Create An Account With Us</li><li>Login To Your Account</li><li>Make A New Payment</li><li>Review &amp; Checkout</li><li>Client Area</li><li>Manage Your Account</li></ul>
    <h4 style="left:670px;top:68px">secure and contact</h4>
    <div class="badge" style="left:670px;top:97px;width:72px;height:24px"></div>
    <div class="badge" style="left:748px;top:97px;width:72px;height:24px"></div>
    <div class="badge" style="left:670px;top:131px;width:70px;height:24px"></div>
    <div class="demo-note">this is for demo reason only</div>
    <div class="contact-box" style="top:195px">EMAIL US :<strong>[EMAIL PROTECTED]</strong></div>
    <div class="contact-box" style="top:249px">CALL US :<strong>00481 62 07 35 18</strong></div>
    <div class="foot-brand"><i></i>Velcor Hub</div>
    <div class="socials"><i></i><i></i><i></i><i></i><i></i><i></i></div>
    <div class="foot-nav" style="left:599px;top:359px">ABOUT US</div>
    <div class="foot-nav" style="left:599px;top:379px">OUR SERVICES</div>
    <div class="foot-nav" style="left:774px;top:359px">PRIVACY POLICY</div>
    <div class="foot-nav" style="left:768px;top:379px">TERMS OF SEVICE</div>
    <div class="copyright">© Copyright 2020 velcor hub</div>
    <div class="locale"><span>English</span><span>United States</span></div>
    <div class="to-top"><svg width="24" height="24" viewBox="0 0 24 24"><path d="M8 14 L12 10 L16 14" fill="none" stroke="#fff" stroke-width="1.6"/></svg></div>
  </footer>

</div>
</body>
</html>
```